Advanced training flyer for defence industry - professional

U.S. Export Controls are some of the most complex and stringent in the world. The U.S. Government regulates the transfer of U.S. origin goods and technical data throughout the world, with the intent of preventing unauthorised transfer of technology and know-how.

These controls extend world-wide and can impact anyone dealing in U.S. controlled goods or technology.

This three-day advanced course is designed to give attendees a greater understanding of U.S. Export Controls from a non-U.S. perspective in practical and relevant terms. Though we will cover a lot of material the course is designed for practitioner with an existing knowledge.

We need a flyer design for an advanced course for the previously mentioned content.

Please include text boxes in order for the form to be completed online.

defence industry

Training

• Please include text boxes so that the form can be completed online.
• flags incorporated

```html
<!DOCTYPE html>
<html lang="en">
<head>
<meta charset="utf-8">
<title>Advanced Defence, EAR &amp; ITAR Training</title>
<link rel="stylesheet" href="https://fonts.googleapis.com/css2?family=Arimo:ital,wght@0,400;0,700;1,400&family=Cormorant+Garamond:wght@500&family=Roboto+Condensed:wght@700&family=Noto+Serif:ital,wght@1,700&display=swap">
<style>
:root{
  --olive:#6e8f2b;
  --lime:#a8c23a;
  --green-text:#6a9a2b;
  --yellow:#f2ea4a;
  --red:#c8202a;
  --ink:#2b2b2b;
  --grey-bg:#eeeeee;
  --page-bg:#7a7a7a;
  --rule:#b9b9b9;
  --sky:#e6f1f8;
}
*{box-sizing:border-box;margin:0;padding:0}
html,body{width:842px;height:1200px;overflow:hidden}
body{background:var(--page-bg);position:relative;font-family:Arimo,Arial,sans-serif;color:var(--ink)}
.panel{position:absolute;left:41px;width:760px;background:#fff;overflow:hidden}
.panel--outside{top:45px;height:536px}
.panel--inside{top:618px;height:535px}

/* ---------- registration form ---------- */
.form-col{position:absolute;left:0;top:0;width:243px;height:536px;font-size:7.4px}
.form-col__band{height:20px;background:var(--lime)}
.form-col__band--bottom{position:absolute;bottom:0;left:0;width:243px;height:17px}
.form-block{padding:6px 16px 4px 16px}
.form-title{color:var(--green-text);font-weight:700;font-size:9.5px;margin:4px 0 5px}
.form-sub{color:var(--green-text);font-weight:700;font-size:8px;margin-bottom:3px}
.field{display:flex;align-items:flex-end;height:12px}
.field label{white-space:nowrap}
.field--indent label{padding-left:40px}
.field input[type=text]{flex:1;border:none;border-bottom:0.6px solid var(--rule);background:transparent;font:7.5px Arimo,Arial,sans-serif;height:10px;margin-left:3px;min-width:0}
.field--gap{margin-bottom:4px}
.form-grey{background:var(--grey-bg);padding:5px 16px 6px;border-top:0.6px solid var(--rule)}
.fee-row{display:flex;justify-content:space-between;margin-bottom:4px;line-height:1.22}
.fee-row b{font-weight:700}
.check{display:inline-flex;align-items:center;gap:2px;white-space:nowrap}
.check input{width:7px;height:7px;margin:0;accent-color:var(--olive)}
.pay-row{display:flex;justify-content:space-between;margin-bottom:3px}
.form-note{padding:6px 16px;line-height:1.28}
.form-note p{margin-bottom:5px}

/* ---------- info column ---------- */
.info-col{position:absolute;left:243px;top:0;width:137px;height:536px;background:var(--olive);color:#fff;font-size:7.6px;line-height:1.28;padding:28px 12px 0 14px}
.info-col h3{color:var(--lime);font-size:7.8px;font-weight:700;margin-top:10px}
.info-col ul{list-style:none;margin-top:3px}
.info-col li{position:relative;padding-left:14px;margin-bottom:4px}
.info-col li::before{content:"";position:absolute;left:2px;top:3px;width:4px;height:4px;border-radius:50%;background:#fff}
.info-col sup{font-size:5px}
.brand-mini{position:absolute;left:20px;bottom:38px;display:flex;align-items:center;gap:5px;font-size:8px;font-weight:700;color:var(--lime);width:100px;line-height:1.1}
.brand-mini .dot{width:16px;height:16px;border-radius:50%;background:var(--lime);flex:none}

/* ---------- cover ---------- */
.cover{position:absolute;left:380px;top:0;width:380px;height:536px;background:#fff}
.brand{position:absolute;left:28px;top:26px;display:flex;align-items:center;gap:10px;color:var(--green-text);font-weight:700;font-size:16px;line-height:1.1;width:220px}
.brand .dot{width:52px;height:52px;border-radius:50%;background:var(--green-text);flex:none}
.cover__title{position:absolute;left:10px;top:150px;font-family:"Cormorant Garamond",Georgia,serif;font-weight:500;color:var(--green-text);font-size:60px;letter-spacing:1px;line-height:1}
.cover__sub{position:absolute;left:12px;top:220px;font-family:"Cormorant Garamond",Georgia,serif;font-weight:500;font-size:16.5px;color:#333}
.cover__dates{position:absolute;left:130px;top:252px;font-size:9.4px;font-weight:700;color:#333;line-height:1.3}
.cover__dates .program{margin-top:9px}
.cover__art{position:absolute;left:0;top:320px;width:380px;height:216px}

/* ---------- inside ---------- */
.voices{position:absolute;left:0;top:0;width:123px;height:535px;background:var(--olive);color:#fff}
.voices__rule{position:absolute;left:52px;top:122px;width:66px;height:2px;background:var(--yellow)}
.voices__lead{position:absolute;left:8px;top:130px;width:108px;text-align:right;font-size:9.4px;line-height:1.3}
.voices__quotes{position:absolute;left:6px;top:272px;width:113px;text-align:right;font-family:"Noto Serif",Georgia,serif;font-style:italic;font-weight:700;font-size:8.3px;line-height:1.28}
.voices__quotes p{margin-bottom:6px}
.voices__mark{position:absolute;font-family:"Noto Serif",Georgia,serif;font-size:84px;color:#fff;opacity:.18;line-height:1}

.intro{position:absolute;left:123px;top:0;width:257px;height:535px;background:#fff}
.intro__text{position:absolute;left:13px;top:30px;width:232px;font-size:7.8px;line-height:1.25}
.intro__text p{margin-bottom:7px}
.lead{color:var(--green-text);font-weight:700;font-size:10.4px}
.price{position:absolute;left:13px;top:180px;font-family:"Roboto Condensed",Arial,sans-serif;font-weight:700;font-size:22px;line-height:1.15;color:var(--green-text)}
.intro__art{position:absolute;left:0;top:222px;width:257px;height:313px}
.attend{position:absolute;left:15px;top:266px;width:225px;font-size:7.8px;line-height:1.25}
.attend h2{font-size:12.5px;font-weight:700;margin-bottom:5px}
.attend p{margin-bottom:5px}

.schedule{position:absolute;left:380px;top:0;width:380px;height:535px;background:linear-gradient(180deg,#f6fafc 0%,var(--sky) 100%)}
.day{position:absolute;top:35px;width:104px;font-size:6.3px;line-height:1.14}
.day h2{background:var(--olive);color:#fff;text-align:center;font-size:10.6px;font-weight:700;height:19px;line-height:19px;margin-bottom:10px}
.day h3{font-size:7.4px;font-weight:700;margin-bottom:3px}
.day h4{font-size:6.4px;font-weight:700;margin-top:4px}
.day ul{list-style:none}
.day li{position:relative;padding-left:7px}
.day li::before{content:"";position:absolute;left:1px;top:2.3px;width:2.6px;height:2.6px;border-radius:50%;background:var(--ink)}
.day ul ul li{padding-left:8px}
.day ul ul li::before{background:none;border:.6px solid var(--ink)}
.day--1{left:12px}
.day--2{left:131px}
.day--3{left:250px;width:118px}
.day--2 h2,.day--3 h2{width:104px}
</style>
</head>
<body>

<!-- Outside: registration, details, cover -->
<section class="panel panel--outside">
  <form class="form-col" aria-label="Seminar registration">
    <div class="form-col__band"></div>
    <div class="form-block">
      <h2 class="form-title">SEMINAR REGISTRATION Venue:</h2>
      <div class="field"><label>Attendee 1 Name :</label><input type="text"></div>
      <div class="field field--indent field--gap"><label>email :</label><input type="text"></div>
      <div class="field"><label>Attendee 2 Name :</label><input type="text"></div>
      <div class="field field--indent field--gap"><label>email :</label><input type="text"></div>
      <div class="field"><label>Attendee 3 Name :</label><input type="text"></div>
      <div class="field field--indent field--gap"><label>email :</label><input type="text"></div>
      <div class="field"><label>Attendee 4 Name :</label><input type="text"></div>
      <div class="field field--indent field--gap"><label>email :</label><input type="text"></div>
    </div>
    <div class="form-grey">
      <h3 class="form-sub">Company:</h3>
      <div class="field"><label>Address:</label><input type="text"></div>
      <div class="field"><label>City:</label><input type="text"><label>&nbsp;Postcode:</label><input type="text"></div>
      <div class="field"><label>Phone:</label><input type="text"><label>&nbsp;Mobile no:</label><input type="text"></div>
    </div>
    <div class="form-block">
      <h3 class="form-sub">FEE</h3>
      <div class="fee-row"><span><b>Defence&amp; ITAR Training</b><br>7 &amp; 8 September – Melbourne<br>21 &amp; 22 September - Sydney</span><span class="check"><input type="checkbox"> $1395</span></div>
      <div class="fee-row"><span><b>ADVANCED Defence&amp; ITAR Training</b><br>9, 10, 11 September – Melbourne<br>23, 24, 25 September - Sydney</span><span class="check"><input type="checkbox"> $2295</span></div>
      <div class="fee-row"><span>Or register for <b>BOTH</b> sessions</span><span class="check"><input type="checkbox"> $3295</span></div>
      <div class="fee-row"><span>Additional copies of workbook</span><span class="check"><input type="checkbox"> $ 99</span></div>
    </div>
    <div class="form-grey">
      <h3 class="form-sub">PAYMENT</h3>
      <div class="pay-row"><span>Payment method:</span><span class="check"><input type="checkbox"> Invoice</span><span class="check"><input type="checkbox"> Credit card</span></div>
      <div class="pay-row"><span>Card type:</span><span class="check"><input type="checkbox"> Card A</span><span class="check"><input type="checkbox"> Card B</span><span class="check"><input type="checkbox"> Card C</span></div>
      <div class="field"><label>Card name &nbsp;&nbsp;&nbsp;&nbsp;&nbsp;&nbsp;:</label><input type="text"></div>
      <div class="field"><label>Card number &nbsp;&nbsp;:</label><input type="text"></div>
      <div class="field"><label>Expiry date &nbsp;&nbsp;&nbsp;&nbsp;:</label><input type="text"><label>&nbsp;CVV:</label><input type="text"></div>
      <div class="field"><label>Cardholder email :</label><input type="text"></div>
    </div>
    <div class="form-note">
      <p>Note: Credit card payments incur a 3% surcharge. Card C incurs 4%.</p>
      <p>Email registrations to info@tradecompliance.example<br>Fax to +61 (0)7 5550 0142</p>
    </div>
    <div class="form-col__band form-col__band--bottom"></div>
  </form>

  <aside class="info-col">
    <h3 style="margin-top:0">Venue:</h3>
    <p>Harbourline Hotel<br>Quay Street, Sydney</p>
    <p style="margin-top:8px">Riverbank Hotel<br>Southgate Lane, Melbourne</p>
    <h3>POLICIES</h3>
    <p>Cancellation<br>Cancellations incur a 20% administration fee. No cancellations permitted within 30 days of training commencing.<br>If a registered attendee is unable to attend, a replacement attendee is allowed.</p>
    <h3>Workbook</h3>
    <p>Each attendees will receive a workbook. The workbook is licenced for the use of the training attendee only. If you need other copies , please order them directly.</p>
    <h3>Multiple attendees</h3>
    <p>Attendees from the same company booked and paid for at the same time for the same course will received the below discounts:</p>
    <ul>
      <li>5 attendees<br>50% discount on the 6<sup>th</sup> attendee.</li>
      <li>10 attendees<br>11<sup>th</sup> attendee free</li>
      <li>&lt; 10 attendees – contact us</li>
    </ul>
    <div class="brand-mini"><span class="dot"></span><span>Institute for Trade Compliance</span></div>
  </aside>

  <div class="cover">
    <div class="brand"><span class="dot"></span><span>Institute for Trade Compliance</span></div>
    <h1 class="cover__title">ADVANCED</h1>
    <p class="cover__sub">DEFENCE, EAR &amp; ITAR Training</p>
    <div class="cover__dates">
      <p>3-day course<br>9, 10, 11 September – Melbourne<br>21, 22, 23 September – Sydney</p>
      <p class="program">Program: 0900 to 1630 each day</p>
    </div>
    <svg class="cover__art" viewBox="0 0 380 216" preserveAspectRatio="none">
      <defs>
        <linearGradient id="coverPhoto" x1="0" y1="0" x2="1" y2="1">
          <stop offset="0" stop-color="#b8292f"/>
          <stop offset=".35" stop-color="#e9e4e4"/>
          <stop offset=".6" stop-color="#2a3f7a"/>
          <stop offset="1" stop-color="#9aa3a8"/>
        </linearGradient>
      </defs>
      <rect role="img" aria-label="Photo: US and Australian flags behind a naval helicopter landing on a ship deck" x="0" y="30" width="380" height="186" fill="url(#coverPhoto)"/>
      <polygon points="0,22 380,0 380,40 0,50" fill="#fff"/>
      <polygon points="0,10 380,18 380,34 0,36" fill="var(--yellow)"/>
      <polygon points="280,44 380,34 380,50" fill="var(--red)"/>
    </svg>
  </div>
</section>

<!-- Inside: overview and three-day program -->
<section class="panel panel--inside">
  <aside class="voices">
    <div class="voices__rule"></div>
    <p class="voices__lead">Guest presenters will deliver different aspects of the training program.</p>
    <span class="voices__mark" style="left:6px;top:240px">“</span>
    <div class="voices__quotes">
      <p>“Extremely well organized and presented, very informative”</p>
      <p>“The Presenter was top rate”</p>
      <p>“Excellent overview of a complex topic”</p>
      <p>“A ‘must-do’ course for anyone working with defence articles”</p>
      <p>“Excellent presentation of a potentially dry subject”</p>
      <p>“Excellent course even for previously trained and experienced Practitioners”</p>
      <p>“Extremely worthwhile”</p>
    </div>
    <span class="voices__mark" style="left:80px;top:478px">”</span>
  </aside>

  <div class="intro">
    <div class="intro__text">
      <p><span class="lead">U.S. Export Controls</span> are some of the most complex and stringent in the world. The U.S. Government regulates the transfer of U.S. origin goods and technical data throughout the world, with the intent of preventing unauthorised transfer of technology and know-how.</p>
      <p>These controls extend world-wide and can impact anyone dealing in U.S. controlled goods or technology.</p>
      <p><span class="lead">This three-day advanced course</span> is designed to give attendees a greater understanding of U.S. Export Controls from a non-U.S. perspective in practical and relevant terms. Though we will cover a lot of material the course is designed for practitioner with an existing knowledge.</p>
    </div>
    <p class="price">$2295.00 AUD<br>per person inc GST</p>
    <svg class="intro__art" viewBox="0 0 257 313" preserveAspectRatio="none">
      <defs>
        <linearGradient id="jetPhoto" x1="0" y1="0" x2="0" y2="1">
          <stop offset="0" stop-color="#eef4f8"/>
          <stop offset=".5" stop-color="#c9d6de"/>
          <stop offset="1" stop-color="#8f9ea8"/>
        </linearGradient>
      </defs>
      <rect role="img" aria-label="Photo: grey fighter jet in flight against a pale sky" x="0" y="150" width="257" height="163" fill="url(#jetPhoto)"/>
      <polygon points="0,30 257,0 257,128 0,172" fill="var(--yellow)"/>
      <polygon points="40,172 257,130 257,160" fill="var(--red)"/>
      <polygon points="0,172 257,160 257,178 0,186" fill="#fff" opacity=".6"/>
    </svg>
    <div class="attend">
      <h2>Who should attend:</h2>
      <p>Practitioners that work for companies that deal with U.S. based technology or that purchase U.S origin products, components or technology.</p>
      <p>The Advanced course assumes a basic understand of U.S. trade controls.</p>
    </div>
  </div>

  <div class="schedule">
    <div class="day day--1">
      <h2>DAY 1</h2>
      <h3>EAR</h3>
      <h4>Introduction</h4>
      <ul><li>Key concepts</li><li>Export Administration Regulations</li><li>Bureau of Industry &amp; Security</li></ul>
      <h4>How To Classify Your Item</h4>
      <ul><li>How to determine the Export Control Classification Number</li></ul>
      <h4>Technology Controls</h4>
      <ul><li>What technology is subject to EAR;</li><li>License exceptions</li><li>Foreign items incorporating controlled U.S.-origin technology</li><li>Encryption under the EAR</li></ul>
      <h4>Technical data Considerations</h4>
      <ul><li>Controls on physical and intangible data</li><li>Deemed export and re-exports</li><li>Third country national issues</li></ul>
      <h4>EAR Exceptions</h4>
      <ul><li>Terms, provisions, applicability and use of Licence Exceptions</li><li>Changes to Exceptions</li><li>Restrictions governing the use of Exceptions</li><li>Distinction between list based and transaction based Licence Exceptions</li></ul>
      <h4>Deemed Export</h4>
      <ul><li>How to determine when deemed export licenses are necessary</li></ul>
      <h4>Export Control Reform</h4>
      <ul><li>ITAR to EAR</li><li>600 series</li><li>Specially designed</li><li>Handling licenses and approvals</li></ul>
    </div>

    <div class="day day--2">
      <h2>DAY 2</h2>
      <h3>ITAR</h3>
      <h4>Introduction</h4>
      <ul><li>Key concepts</li><li>International Traffic in Arms Regulations</li></ul>
      <h4>Understanding ITAR classifications</h4>
      <h4>How to classify an item in the ITAR</h4>
      <h4>Re-exports &amp; re-transfers</h4>
      <ul><li>Licence free activity</li><li>Returning items to the U.S.</li></ul>
      <h4>ITAR approvals</h4>
      <ul><li>Licences</li><li>Agreements
        <ul><li>Types of agreements</li><li>Sub-licensing</li><li>Dual nationals</li><li>NDA's</li><li>Amendments</li></ul></li></ul>
      <h4>Brokering</h4>
      <ul><li>Extra-territorial application</li><li>Registration</li><li>Reporting requirements</li></ul>
      <h4>Destruction and Disposal of ITAR items</h4>
      <h4>Defence services involving ITAR controlled articles and technical data</h4>
      <h4>Recordkeeping for the ITAR</h4>
      <h4>Foreign Military Sales</h4>
      <ul><li>Letter of Offer</li><li>Third Party Re-transfer Approvals</li><li>Export Control Reform and FMS</li></ul>
      <h4>Export Control Reform</h4>
      <ul><li>The ITAR definition of Specially Designed</li></ul>
    </div>

    <div class="day day--3">
      <h2>DAY 3</h2>
      <h4 style="margin-top:0">COMPLIANCE &amp; ENFORCEMENT</h4>
      <h4>Trade Control Compliance Framework</h4>
      <ul><li>Document development</li><li>Infrastructure</li><li>Risk assessments</li><li>Internal self assessments</li></ul>
      <h4>Enforcement</h4>
      <ul><li>U.S. enforcement</li><li>Fines and penalties</li><li>Case studies</li><li>Preventing violations</li></ul>
      <h4>NON-US ISSUES<br>Dual Nationals</h4>
      <ul><li>Anti-discrimination</li><li>Privacy</li></ul>
      <h4>AUSTRALIAN REGULATIONS</h4>
      <ul><li>Australia's System of Export Controls</li><li>Defence and Strategic Goods List?</li><li>Dual-Use List</li><li>Customs Act 1901</li><li>Defence Trade Controls Act 2012</li><li>Catch-All Legislation</li><li>Sanctions Legislation</li><li>Compliance philosophy</li><li>Non-compliance and penalties</li><li>Risk of diversion</li><li>Cyber security</li><li>Red flags</li><li>Self-Assessment Tool</li><li>AU-US Trade Co-operation Treaty</li><li>Managing the transition to intangibles</li></ul>
    </div>
  </div>
</section>

</body>
</html>
```